Portal Panel Medic need professional looking business card printed on plastic, Commericial, Industri

We are family owned and operated garage door company in Indianapolis, Indiana. We sale service and install dock equipment, doors, operators. We are looking to expand our commercial/ industrial division. We also service all residential doors and operators. We are looking for a business that stands out of the crowd. We are committed to have the best customer service in the industry.

Target Market(s)

National and local general contractors, National/ Corpate service accounts,

Industry/Entity Type

Business Service

Contact Information for Business Card

To be printed on plastic stock

Font styles to use
Sans Serif

Colors
ffffff
f04a50
ec1f27

Requirements
Must have
• Name, website,email, phone number, position.
Nice to have
• A standout professional design

```html
<!DOCTYPE html>
<html lang="en">
<head>
<meta charset="utf-8">
<title>Portal Panel Medic — Business Card</title>
<link rel="stylesheet" href="https://fonts.googleapis.com/css2?family=Roboto+Condensed:wght@700&family=Roboto:wght@300;400&display=swap">
<style>
  :root {
    --backdrop: #e4e4e4;
    --panel-light: #e6e3dd;
    --panel-light-shade: #cfcbc3;
    --brand-red: #ec1f27;
    --red-deep: #b81b1a;
    --red-dark: #5a0b0b;
    --divider: #111111;
    --ink-white: #ffffff;
    --ink-soft: #f3dada;
  }
  * { box-sizing: border-box; margin: 0; padding: 0; }
  html, body {
    width: 1200px; height: 900px; overflow: hidden;
    background: var(--backdrop);
  }
  .canvas {
    position: relative; width: 1200px; height: 900px;
    display: flex; align-items: center; justify-content: center;
  }
  .business-card {
    position: relative; width: 1000px; height: 572px;
    border-radius: 28px; overflow: hidden;
    background: linear-gradient(135deg, var(--red-deep) 0%, #9c1514 45%, var(--red-dark) 100%);
    box-shadow: 0 18px 40px rgba(0,0,0,0.18);
  }
  .card-shapes { position: absolute; inset: 0; width: 100%; height: 100%; }
  .brand-lockup {
    position: absolute; left: 100px; top: 180px;
    display: flex; align-items: center; gap: 22px;
  }
  .mascot-area {
    width: 110px; height: 190px; border-radius: 10px;
    background: linear-gradient(180deg, #a9a6a0 0%, #7d6a60 55%, #4a3a33 100%);
  }
  .brand-name {
    font-family: "Roboto Condensed", sans-serif; font-weight: 700;
    font-size: 44px; line-height: 1.1;
    color: var(--brand-red); white-space: nowrap;
  }
  .contact-block {
    position: absolute; left: 640px; top: 118px;
    color: var(--ink-white);
  }
  .person-name {
    font-family: "Roboto Condensed", sans-serif; font-weight: 700;
    font-size: 40px; line-height: 1.1;
  }
  .person-role {
    font-family: "Roboto", sans-serif; font-weight: 400;
    font-size: 20px; color: var(--ink-soft); margin-top: 4px;
  }
  .contact-list { list-style: none; margin-top: 38px; }
  .contact-item {
    display: flex; align-items: center; gap: 14px;
    font-family: "Roboto", sans-serif; font-weight: 300;
    font-size: 20px; line-height: 1.6; color: var(--ink-soft);
  }
  .contact-icon { width: 18px; height: 18px; flex: none; fill: var(--ink-soft); }
</style>
</head>
<body>
<main class="canvas">
  <section class="business-card">
    <svg class="card-shapes" viewBox="0 0 1000 572" preserveAspectRatio="none" aria-hidden="true">
      <defs>
        <linearGradient id="panelLight" x1="0" y1="0" x2="1" y2="1">
          <stop offset="0" stop-color="#ebe8e3"/>
          <stop offset="1" stop-color="#cfcbc3"/>
        </linearGradient>
      </defs>
      <path d="M0,0 H548 C640,110 665,410 612,572 H0 Z" fill="var(--divider)"/>
      <path d="M0,0 H530 C622,110 646,410 596,572 H0 Z" fill="url(#panelLight)"/>
    </svg>

    <div class="brand-lockup">
      <div class="mascot-area" role="img" aria-label="Cartoon mascot of a repair doctor with a stethoscope"></div>
      <p class="brand-name">Portal Panel Medic</p>
    </div>

    <div class="contact-block">
      <h1 class="person-name">Jordan Ames Reed</h1>
      <p class="person-role">Managing Director</p>
      <ul class="contact-list">
        <li class="contact-item">
          <svg class="contact-icon" viewBox="0 0 24 24" aria-hidden="true"><path d="M6.6 10.8a15 15 0 0 0 6.6 6.6l2.2-2.2a1 1 0 0 1 1-.25 11.4 11.4 0 0 0 3.6.57 1 1 0 0 1 1 1V20a1 1 0 0 1-1 1A17 17 0 0 1 3 4a1 1 0 0 1 1-1h3.5a1 1 0 0 1 1 1c0 1.25.2 2.450.57 3.57a1 1 0 0 1-.25 1z"/></svg>
          (317) 555-0148
        </li>
        <li class="contact-item">
          <svg class="contact-icon" viewBox="0 0 24 24" aria-hidden="true"><path d="M2 5h20v14H2zM4 7v.5l8 5 8-5V7l-8 5z"/></svg>
          jordan@portalpanelmedic.com
        </li>
        <li class="contact-item">
          <svg class="contact-icon" viewBox="0 0 24 24" aria-hidden="true"><path d="M12 2a10 10 0 1 0 0 20 10 10 0 0 0 0-20zm6.9 9h-3a15 15 0 0 0-1.3-5.6A8 8 0 0 1 18.9 11zM12 4.1c.9 1.3 1.8 3.7 1.9 6.9h-3.8c.1-3.2 1-5.6 1.9-6.9zM9.4 5.4A15 15 0 0 0 8.1 11h-3a8 8 0 0 1 4.3-5.6zM5.1 13h3a15 15 0 0 0 1.3 5.6A8 8 0 0 1 5.1 13zm6.9 6.9c-.9-1.3-1.8-3.7-1.9-6.9h3.8c-.1 3.2-1 5.6-1.9 6.9zm2.6-1.3a15 15 0 0 0 1.3-5.6h3a8 8 0 0 1-4.3 5.6z"/></svg>
          www.portalpanelmedic.com
        </li>
      </ul>
    </div>
  </section>
</main>
</body>
</html>
```